Awesome Office Furniture Dealer's Brochure!

Need a professional and informative brochure put together for our clients - may need separate designs for Government and Education clients. Should be based of our new website design and feel. Sections should include: Manufacturers we carry, services, and statements about our company - who we are & what we do. Brochure is 8.5 x 11 in tri-fold configuration. Template files attached.

Target Market(s)

Small to Medium businesses

Industry/Entity Type

Office Furniture

Requirements
Must have
• Look and feel of our website www.pelmaro.com. Images can be taken from any of our vendors listed under /products, look to VEX primarily. We will get the final designer production ready images when needed.
Nice to have
• Incorporate the "love your workspace" from our website.

```html
<!DOCTYPE html>
<html lang="en">
<head>
<meta charset="utf-8">
<title>Pelmaro Office Furniture – Brochure Panel</title>
<link href="https://fonts.googleapis.com/css2?family=Great+Vibes&family=Montserrat:wght@600&family=Questrial&display=swap" rel="stylesheet">
<style>
  :root {
    --green: #6ab42f;
    --slate: #6b6c70;
    --slate-light: #8d8e91;
    --slate-soft: #7b7c80;
    --ink: #6a6b6e;
    --white: #ffffff;
  }
  * { margin: 0; padding: 0; box-sizing: border-box; }
  html, body { width: 1200px; height: 930px; overflow: hidden; background: var(--white); }
  .brochure {
    position: relative; width: 1200px; height: 930px;
    display: grid; grid-template-columns: 406px 398px 396px;
    font-family: "Questrial", sans-serif;
  }
  .panel { position: relative; display: flex; flex-direction: column; }
  .panel-head { height: 220px; text-align: center; position: relative; }
  .script-we {
    font-family: "Great Vibes", cursive; font-size: 104px; line-height: 1;
    position: absolute; left: 0; right: 0; top: 18px;
  }
  .headline {
    font-family: "Montserrat", sans-serif; font-weight: 600; font-size: 82px;
    letter-spacing: -2px; line-height: 1; position: absolute; left: 0; right: 0; top: 126px;
  }
  .photo { height: 222px; }
  .copy { text-align: center; font-size: 27px; line-height: 33px; }

  /* Know */
  .panel-know .script-we, .panel-know .headline { color: var(--green); }
  .panel-know .photo { background: linear-gradient(135deg, #e9edf1, #9a9ca3 55%, #3b3d44); }
  .panel-know .copy-block { flex: 1; background: var(--green); color: var(--white); padding-top: 16px; }
  .panel-know .copy + .copy { margin-top: 32px; }

  /* Value */
  .panel-value { background: var(--slate); color: var(--white); }
  .value-divider {
    display: block; width: 340px; height: 56px; margin: 8px auto 0;
    background: var(--slate-soft);
  }
  .panel-value .intro { margin-top: 20px; font-size: 27px; line-height: 30px; }
  .panel-value .tag-photo { position: absolute; top: 442px; left: 0; right: 0; height: 195px;
    background: linear-gradient(160deg, #a4a5a8, var(--slate-light) 60%, #7c7d80); }
  .panel-value .closing { position: absolute; top: 664px; left: 0; right: 0; font-size: 30px; line-height: 36px; }
  .panel-value .closing .you { font-size: 36px; }

  /* Offer */
  .panel-offer .script-we, .panel-offer .headline { color: var(--green); }
  .panel-offer .photo { background: linear-gradient(150deg, #f4f4f2, #d9d9d6 55%, #c9b34a 85%, #d44a2a); }
  .panel-offer .copy-block { height: 195px; color: var(--ink); padding-top: 14px; }
  .panel-offer .copy { font-size: 27px; line-height: 30px; }
  .panel-offer .crew-photo { flex: 1; position: relative;
    background: linear-gradient(170deg, #dfe6ea, #b9c1c6 45%, #8a8f93 75%, #b86a3a); }
  .brand-name {
    position: absolute; right: 36px; bottom: 34px; text-align: right;
    font-family: "Questrial", sans-serif; color: var(--green);
    font-size: 66px; line-height: 1; letter-spacing: 0;
  }
  .brand-name small { display: block; font-size: 18px; letter-spacing: 6.5px; margin-top: 8px; }
</style>
</head>
<body>
<main class="brochure">
  <section class="panel panel-know">
    <header class="panel-head">
      <div class="script-we">We</div>
      <h2 class="headline">KNOW</h2>
    </header>
    <div class="photo" role="img" aria-label="Photo of a smiling business team in suits"></div>
    <div class="copy-block">
      <p class="copy">With over 30 years<br>of experience in<br>commercial furniture,<br>we know what we are doing.</p>
      <p class="copy">You can count on our<br>knowledgeable staff<br>to help you through the<br>entire buying process.<br>From design to product<br>choice to final installation,<br>we will be with you<br>every step of the way.</p>
    </div>
  </section>

  <section class="panel panel-value">
    <header class="panel-head">
      <div class="script-we">We</div>
      <h2 class="headline">VALUE</h2>
    </header>
    <div class="value-divider" role="img" aria-label="Decorative arrow graphic with a heart"></div>
    <p class="copy intro">We don’t “push” specific items<br>because they cost more, or<br>because some manufacturer<br>wants us to.</p>
    <div class="tag-photo" role="img" aria-label="Photo of a blank paper price tag on string"></div>
    <p class="copy closing">We value our customers<br>and only sell products<br>that we believe<br>represent value<br>to <span class="you">YOU.</span></p>
  </section>

  <section class="panel panel-offer">
    <header class="panel-head">
      <div class="script-we">We</div>
      <h2 class="headline">OFFER</h2>
    </header>
    <div class="photo" role="img" aria-label="Photo of floor plans, a tape measure and colour swatches"></div>
    <div class="copy-block">
      <p class="copy">We offer design<br>and space-planning<br>and affordable delivery<br>and installation by our<br>in-house crew.</p>
    </div>
    <div class="crew-photo" role="img" aria-label="Photo of two installers assembling a desk in an office">
      <div class="brand-name">PELMARO<small>OFFICE FURNITURE</small></div>
    </div>
  </section>
</main>
</body>
</html>
```